Velor Stationery Design

We need Business Card, Letterhead, #10 Envelope , 3" x 4" Mailing Label, and email signature block. Also need "Aircraft Services" added small under the logo on everything except the email signature block. "Aircraft Services" should be in a simple font to to conflict with or distract from the logo. Our address info is:
4817 Marlow Bend NW
Larkfield, GA 30871
P 555.284.6613
C 555.284.6613 (for biz cards only)
pete@velorjet.example (for biz cards only)
Website velorjet.example
Feel free to play around with colors but I expect that black or gray will work best for the address/phone info etc.

Target Market(s)

Aircraft owners

Industry/Entity Type

Aviation

Colors

Designer to choose only greyscale colors for use in the design.

Requirements
Must have
• Clean and sophisticated design -

```html
<!DOCTYPE html>
<html lang="en">
<head>
<meta charset="utf-8">
<title>Velor Stationery Design</title>
<link href="https://fonts.googleapis.com/css2?family=Roboto:wght@400;700&display=swap" rel="stylesheet">
<style>
  :root {
    --backdrop: #39393b;
    --paper: #f5f3f3;
    --card: #ffffff;
    --brand-blue: #0a7cdb;
    --ink: #2b2b2b;
    --ink-soft: #555555;
    --caption: #e6e6e6;
    --rule: #3a3a3a;
  }
  * { box-sizing: border-box; margin: 0; padding: 0; }
  html, body { width: 1200px; height: 613px; overflow: hidden; }
  body {
    background: var(--backdrop);
    font-family: "Roboto", sans-serif;
    color: var(--ink);
    position: relative;
  }
  .piece { position: absolute; }
  .sheet { position: absolute; background: var(--paper); }
  .card { position: absolute; background: var(--card); }
  .rounded { border-radius: 7px; }
  .caption {
    position: absolute;
    font-size: 6px;
    color: var(--caption);
    text-align: center;
    transform: translateX(-50%);
    white-space: nowrap;
  }
  .wordmark {
    position: absolute;
    font-family: "Roboto", sans-serif;
    font-weight: 700;
    color: var(--brand-blue);
    text-transform: uppercase;
    letter-spacing: 0.06em;
    line-height: 1;
    white-space: nowrap;
  }
  .wordmark.on-blue { color: #ffffff; }
  .tagline {
    position: absolute;
    font-size: 6.6px;
    color: var(--ink);
    line-height: 1;
    white-space: nowrap;
  }
  .info {
    position: absolute;
    font-size: 6.8px;
    line-height: 8.4px;
    color: var(--ink);
    white-space: nowrap;
  }
  .info .row { display: flex; align-items: center; gap: 2px; }
  .info .gap { height: 4px; }
  .icon { width: 5px; height: 5px; fill: var(--brand-blue); flex: none; }
  .divider { position: absolute; width: 0.6px; background: var(--rule); }

  /* letterhead */
  .salutation { position: absolute; left: 33px; top: 128px; font-size: 9.2px; color: var(--ink-soft); }
  .letter-body { position: absolute; left: 33px; top: 152px; width: 270px; }
  .letter-body p {
    font-size: 5.1px;
    line-height: 8px;
    color: var(--ink-soft);
    text-align: justify;
    margin-bottom: 8px;
  }
  .closing { position: absolute; left: 33px; top: 330px; font-size: 4.8px; color: var(--ink-soft); }
  .signature-area { position: absolute; left: 32px; top: 341px; width: 44px; height: 18px; }
  .signer-name { position: absolute; left: 35px; top: 367px; font-size: 7.4px; color: var(--ink-soft); }
  .signer-role { position: absolute; left: 35px; top: 377px; font-size: 5.4px; color: var(--ink-soft); }
</style>
</head>
<body>

<svg width="0" height="0" style="position:absolute" aria-hidden="true">
  <defs>
    <symbol id="icon-phone" viewBox="0 0 10 10">
      <path d="M2.2 0.6 L3.8 2.6 L2.9 3.7 Q4 6 6.3 7.1 L7.4 6.2 L9.4 7.8 L8.3 9.4 Q2.6 8.6 0.6 1.7 Z"/>
    </symbol>
    <symbol id="icon-mobile" viewBox="0 0 10 10">
      <path d="M2.5 0 H7.5 V10 H2.5 Z M3.4 1 V8.2 H6.6 V1 Z"/>
    </symbol>
    <symbol id="icon-mail" viewBox="0 0 10 10">
      <path d="M0.5 2.2 H9.5 V7.8 H0.5 Z M1.2 2.8 L5 5.4 L8.8 2.8 Z" fill-rule="evenodd"/>
    </symbol>
    <symbol id="icon-globe" viewBox="0 0 10 10">
      <circle cx="5" cy="5" r="4.6"/>
      <path d="M5 0.8 V9.2 M0.8 5 H9.2 M2 2.6 Q5 4 8 2.6 M2 7.4 Q5 6 8 7.4" stroke="#fff" stroke-width="0.7" fill="none"/>
    </symbol>
  </defs>
</svg>

<!-- Mailing label -->
<section class="card mailing-label" style="left:115.5px; top:78px; width:181px; height:125px;">
  <div class="wordmark" style="left:0; width:181px; text-align:center; top:24px; font-size:20px;">Velor</div>
  <div class="tagline" style="left:0; width:181px; text-align:center; top:46px;">Aircraft Services</div>
  <div class="info" style="left:0; width:181px; top:61px; text-align:center;">
    <div>4817 Marlow Bend NW</div>
    <div>Larkfield, GA 30871</div>
    <div class="gap"></div>
    <div class="row" style="justify-content:center;">
      <svg class="icon"><use href="#icon-phone"/></svg>555.284.6613
      <svg class="icon" style="margin-left:2px;"><use href="#icon-mobile"/></svg>555.284.6613
    </div>
    <div class="row" style="justify-content:center;">
      <svg class="icon"><use href="#icon-mail"/></svg>pete@velorjet.example
      <svg class="icon" style="margin-left:2px;"><use href="#icon-globe"/></svg>www.velorjet.example
    </div>
  </div>
</section>
<div class="caption" style="left:202px; top:212px;">Mailing Label</div>

<!-- Business card front -->
<section class="card rounded business-card-front" style="left:87px; top:231.5px; width:239px; height:136.5px;">
  <div class="wordmark" style="left:32px; width:82px; text-align:center; top:55px; font-size:19px;">Velor</div>
  <div class="tagline" style="left:32px; width:82px; text-align:center; top:77px;">Aircraft Services</div>
  <div class="divider" style="left:124px; top:35px; height:67px;"></div>
  <div class="info" style="left:136.5px; top:40px;">
    <div>4817 Marlow Bend NW</div>
    <div>Larkfield, GA 30871</div>
    <div class="gap"></div>
    <div class="row"><svg class="icon"><use href="#icon-phone"/></svg>555.284.6613</div>
    <div class="row"><svg class="icon"><use href="#icon-mobile"/></svg>555.284.6613</div>
    <div class="row"><svg class="icon"><use href="#icon-mail"/></svg>pete@velorjet.example</div>
    <div class="row"><svg class="icon"><use href="#icon-globe"/></svg>www.velorjet.example</div>
  </div>
</section>
<div class="caption" style="left:205px; top:378px;">Bussiness Card _Front</div>

<!-- Business card back -->
<section class="card rounded business-card-back" style="left:82px; top:399px; width:244px; height:140px;">
  <div class="wordmark" style="left:0; width:244px; text-align:center; top:51px; font-size:36px;">Velor</div>
</section>
<div class="caption" style="left:192px; top:547px;">Bussiness Card _Back</div>

<!-- Letterhead -->
<section class="sheet letterhead" style="left:354px; top:76px; width:334px; height:471px;">
  <div class="wordmark" style="left:32px; top:37px; font-size:20px;">Velor</div>
  <div class="tagline" style="left:49px; top:58px;">Aircraft Services</div>
  <div class="info" style="left:235px; top:32px;">
    <div>4817 Marlow Bend NW</div>
    <div>Larkfield, GA 30871</div>
    <div class="row"><svg class="icon"><use href="#icon-phone"/></svg>555.284.6613</div>
    <div class="row"><svg class="icon"><use href="#icon-globe"/></svg>www.velorjet.example</div>
  </div>
  <div class="salutation">Dear Mr. Hale,</div>
  <div class="letter-body">
    <p>Thank you for trusting our team with the care of your aircraft this season. Our technicians completed the scheduled inspection and logged every finding in your maintenance record. We found the airframe in excellent condition, with only minor wear on the brake assemblies. Those parts have been replaced and tested, and the aircraft is ready for your next flight whenever you are.</p>
    <p>During the visit we also reviewed the avionics software and applied the latest approved updates. The navigation database is current through the coming cycle, and the autopilot passed all ground checks. A full summary of the work, including part numbers and labor hours, is enclosed with this letter for your files and your records.</p>
    <p>Looking ahead, we recommend booking your annual inspection early, as the spring schedule fills quickly. Our hangar can also arrange detailing, interior refresh and paint touch-ups while the aircraft is in our care. Please let us know which services you would like, and we will prepare a quote within two business days. Our crew can also move the aircraft to and from your home field on request, so the visit fits around your own flying plans.</p>
    <p>If you have any questions about the work performed or your upcoming schedule, our service desk is available every weekday from early morning until evening. You may also reach us by email at any time and expect a reply within one working day. We look forward to seeing you and your aircraft again soon at our hangar.</p>
  </div>
  <div class="closing">Sincerely,</div>
  <div class="signature-area" role="img" aria-label="Handwritten signature of John Hale" style="background:linear-gradient(90deg, rgba(40,40,40,0.08), rgba(40,40,40,0.18), rgba(40,40,40,0.06));"></div>
  <div class="signer-name">John Hale</div>
  <div class="signer-role">CEO/ Founder</div>
</section>
<div class="caption" style="left:515px; top:554px;">Letterhead</div>

<!-- Email signature -->
<section class="card email-signature" style="left:769px; top:150px; width:340px; height:93px;">
  <div class="wordmark" style="left:21.5px; top:17px; font-size:25px;">Velor</div>
  <div class="info" style="left:21.5px; top:58px;">
    <div>4817 Marlow Bend NW</div>
    <div>Larkfield, GA 30871</div>
  </div>
  <div class="divider" style="left:99px; top:58px; height:15px;"></div>
  <div class="info" style="left:109px; top:56px;">
    <div class="row"><svg class="icon"><use href="#icon-phone"/></svg>555.284.6613</div>
    <div class="row"><svg class="icon"><use href="#icon-globe"/></svg>www.velorjet.example</div>
  </div>
</section>
<div class="caption" style="left:868px; top:254px;">Email Signature</div>

<!-- Envelope back with flap -->
<section class="sheet envelope-back" style="left:742px; top:285px; width:375px; height:171px;">
  <svg class="piece" style="left:0; top:0;" width="375" height="62" viewBox="0 0 375 62" aria-hidden="true">
    <path d="M0 0 H375 L367 46 Q364 62 346 62 H30 Q13 62 9 46 Z" fill="var(--brand-blue)"/>
  </svg>
  <div class="wordmark on-blue" style="left:0; width:375px; text-align:center; top:21px; font-size:27px;">Velor</div>
</section>

<!-- Envelope front -->
<section class="sheet envelope-front" style="left:714px; top:376px; width:376px; height:171px; box-shadow:0 0 3px rgba(0,0,0,0.25);">
  <div class="wordmark" style="left:20.5px; top:23px; font-size:21px;">Velor</div>
  <div class="tagline" style="left:36px; top:45px;">Aircraft Services</div>
  <div class="info" style="left:20.5px; top:116px;">
    <div>4817 Marlow Bend NW</div>
    <div>Larkfield, GA 30871</div>
    <div class="gap"></div>
    <div class="row"><svg class="icon"><use href="#icon-phone"/></svg>555.284.6613</div>
    <div class="row"><svg class="icon"><use href="#icon-globe"/></svg>www.velorjet.example</div>
  </div>
</section>
<div class="caption" style="left:902px; top:554px;">Envelope</div>

</body>
</html>
```